Up and Coming Granola Brand Needs Labels and Logo Design

We need a label design for a new Granola Company called Pem's Granola. We create delicious hand-crafted granolas that are not only tasty, but good for you!

We would also like a 'modern' logo, similar to the attached one.
The logo name is "Pem's". The concept would be to have the word "Pem's" in the banner, and "Granola" below in font. Eventually the product line will expand to include other items, and we would like a logo that allows us to match the product to the logo name.

The logo should integrate well with the packaging label.

We plan on using light brown resealable packaging for our granola, and would prefer earthy colours, or colours that would complement the packaging for the labels. We intend to print the designs on labels, and paste them on the front and back of the package. (Package dimensions and image of package are included in attachments)

We plan on having a few flavours of Granola, and that would have some small changes on the label design.

Some of our ingredients in our granola would include Oats, Dried fruit, nuts and various grains.

It would be good if the labels could feature oats (perhaps an ear of oats, or something to similar effect)
Updates

have added dimensions to the packaging to give a sense of size for reference. image of the packaging we will be using also added! Added Wednesday, May 11, 2016

Reason: Loving the submissions so far! Can't wait to see what else you can come up with! Have extended the deadline to give some breathing room and time for tweaking!

Target Market(s)

20s-40s

Industry/Entity Type

Food Store

Logo Text

Pem's

Font styles to use
Serif
Decorative

Requirements
Must have
• -Colours that complement the packaging colour (light brown)
• -Can be printed on white labels that will be stuck on the packaging (both for the front of packaging; that has a window, and the back of the packaging; no window)
• -simple and stylish design that entices buyers to purchase the product
• -A flexible logo that can transition seamlessly between different product lines
• - Sections for "our story", "nutritional information", "ingredients, etc on the back label.
Nice to have
• -as attached in image samples for the brief.
• - other trendy designs that are currently popular
• - different colour schemes for different flavours. Currently there are 3 flavours; 1) Mocha Almond, 2) Matcha with White Chocolate and Cashews, and 3) Classic Fruit and Nut.
Should not have
• -colours that stand out too much, or do not fit the design brief
• -overly complicated designs that take away from the main theme of awesome granola

```html
<!DOCTYPE html>
<html lang="en">
<head>
<meta charset="utf-8">
<title>Pem's Granola – Label Set</title>
<link href="https://fonts.googleapis.com/css2?family=Oswald:wght@400;500;600&family=Dancing+Script:wght@500&family=Roboto:wght@700&display=swap" rel="stylesheet">
<style>
  :root{
    --page:#ffffff;
    --ink:#3a3736;
    --frame:#4a4644;
    --panel:#3b3837;
    --brown:#6b4226;
    --rust:#b8764f;
    --cream:#f5f0da;
    --leaf:#8fc34a;
    --matcha:#b9d49c;
    --matcha-deep:#a6c486;
    --mocha-light:#e6dcc0;
    --mocha-deep:#9d7f4a;
    --gold:#d9cf3c;
    --mocha-text:#b7d48a;
    --nutrition:#e6cfc2;
    --white:#ffffff;
    --dots:#8c8683;
  }
  *{box-sizing:border-box;margin:0;padding:0}
  html,body{width:1200px;height:1200px;overflow:hidden;background:var(--page)}
  .sheet{position:relative;width:1200px;height:1200px}

  /* ---------- front labels ---------- */
  .front{position:absolute;top:230px;width:380px;height:260px}
  .front svg{position:absolute;inset:0}
  .front .brand{position:absolute;left:0;right:0;top:8px;text-align:center;
    font-family:'Oswald',sans-serif;font-weight:600;color:var(--brown);line-height:1}
  .front .brand .name{display:block;font-size:44px;letter-spacing:1px}
  .front .brand .sub{display:block;font-size:17px;letter-spacing:3px;margin-top:2px}
  .front .copy{position:absolute;left:95px;width:190px;top:92px;text-align:center;
    font-family:'Oswald',sans-serif;line-height:1}
  .tagline{font-size:10px;line-height:1;color:#d9d4cc;font-weight:400;display:block;margin-bottom:5px}
  .flavour{display:block;font-weight:500;text-transform:uppercase;line-height:1}
  .dotrule{display:block;margin:6px auto 0;width:150px;border-top:3px dotted var(--dots)}

  .classic{left:20px}
  .classic .f1{font-size:42px;color:var(--rust)}
  .classic .f2{font-size:33px;color:#efe9de;margin-top:3px}
  .classic .amp{color:var(--leaf);font-size:24px}

  .matcha{left:410px}
  .matcha .f1{font-size:36px;color:var(--matcha)}
  .matcha .with{display:block;font-size:10px;line-height:1.1;color:#ddd;text-transform:lowercase}
  .matcha .f2{font-size:17px;color:#f0ede6}
  .matcha .f3{font-size:25px;color:var(--gold);margin-top:2px}

  .mocha{left:800px}
  .mocha .f1,.mocha .f2{font-size:44px;color:var(--mocha-text)}
  .mocha .f2{text-transform:none;margin-top:2px}

  /* ---------- back labels ---------- */
  .back{position:absolute;top:540px;width:352px;height:430px;border-radius:8px;overflow:hidden}
  .back .art{position:absolute;right:0;bottom:0;width:60%;height:45%;opacity:.6}
  .back .story{position:absolute;left:12px;top:14px;width:172px;height:388px;
    background:var(--panel);border-radius:12px;overflow:hidden}
  .story .heading{position:absolute;left:12px;top:8px;font-family:'Dancing Script',cursive;
    font-size:20px;color:var(--leaf)}
  .story .wheat{position:absolute;left:0;bottom:70px;width:100%;height:160px;
    background:linear-gradient(180deg,rgba(80,60,40,0),rgba(105,80,50,.55) 60%,rgba(80,60,40,.2))}
  .story .mini-brand{position:absolute;left:0;right:0;top:272px;text-align:center;
    font-family:'Oswald',sans-serif;font-weight:600;color:var(--cream);line-height:1}
  .mini-brand .name{display:block;font-size:22px}
  .mini-brand .sub{display:block;font-size:9px;letter-spacing:2px;margin-top:2px}
  .story .web{position:absolute;left:8px;right:8px;top:314px;padding:8px 0;text-align:center;
    font-family:'Oswald',sans-serif;font-size:13px;color:var(--white);
    border-top:3px dotted #6b6562;border-bottom:3px dotted #6b6562}
  .back .nutrition{position:absolute;left:190px;top:14px;width:150px;height:286px;background:var(--nutrition)}
  .nutrition h2{font-family:'Roboto',sans-serif;font-size:16px;color:var(--ink);padding:6px 10px}
  .nutrition .ingredients{position:absolute;left:10px;top:196px;font-family:'Roboto',sans-serif;
    font-size:7px;color:var(--ink)}
  .back .upc{position:absolute;left:190px;top:312px;width:146px;height:72px;background:var(--white);
    border:1px solid #555;display:flex;align-items:center;justify-content:center;
    font-family:'Oswald',sans-serif;font-size:13px;color:var(--ink)}
  .back.classic-bg{left:34px;background:linear-gradient(160deg,var(--cream),#f3efd6 60%,#e7edc8)}
  .back.matcha-bg{left:424px;background:linear-gradient(160deg,var(--matcha),#c9ddb0 60%,var(--matcha-deep))}
  .back.mocha-bg{left:814px;background:linear-gradient(160deg,var(--mocha-light),#cfb98c 60%,var(--mocha-deep))}
</style>
</head>
<body>
<main class="sheet">

  <section class="front classic">
    <svg viewBox="0 0 380 260" width="380" height="260">
      <defs>
        <linearGradient id="bgClassic" x1="0" y1="0" x2="1" y2="1">
          <stop offset="0" stop-color="#f6f2dc"/><stop offset="1" stop-color="#e9eec6"/>
        </linearGradient>
      </defs>
      <path d="M2 36 H70 Q120 2 190 2 Q260 2 310 36 H378 V248 H310 Q260 262 190 262 Q120 262 70 248 H2 Z" fill="url(#bgClassic)" stroke="#4a4644" stroke-width="3"/>
      <rect x="12" y="100" width="78" height="140" fill="#d9b98d" opacity=".45" role="img" aria-label="Illustration of wheat and oat ears"/>
      <rect x="292" y="100" width="78" height="140" fill="#e2d6b4" opacity=".4" role="img" aria-label="Illustration of wheat and oat ears"/>
      <polygon points="95,82 285,82 285,238 190,222 95,238" fill="#3b3837" stroke="#fff" stroke-width="3"/>
    </svg>
    <div class="brand"><span class="name">Pem's</span><span class="sub">GRANOLA</span></div>
    <div class="copy">
      <span class="tagline">not only tasty, but good for you!</span>
      <span class="flavour f1">Classic</span>
      <span class="flavour f2">Fruit<span class="amp">&amp;</span>Nut</span>
      <span class="dotrule"></span>
    </div>
  </section>

  <section class="front matcha">
    <svg viewBox="0 0 380 260" width="380" height="260">
      <path d="M2 36 H70 Q120 2 190 2 Q260 2 310 36 H378 V248 H310 Q260 262 190 262 Q120 262 70 248 H2 Z" fill="#b9d49c" stroke="#4a4644" stroke-width="3"/>
      <rect x="12" y="100" width="78" height="140" fill="#c9a36c" opacity=".4" role="img" aria-label="Illustration of wheat and oat ears"/>
      <rect x="292" y="100" width="78" height="140" fill="#cfe0b5" opacity=".6" role="img" aria-label="Illustration of wheat and oat ears"/>
      <polygon points="95,82 285,82 285,238 190,222 95,238" fill="#3b3837" stroke="#fff" stroke-width="3"/>
    </svg>
    <div class="brand"><span class="name">Pem's</span><span class="sub">GRANOLA</span></div>
    <div class="copy">
      <span class="tagline">not only tasty, but good for you!</span>
      <span class="flavour f1">Matcha</span>
      <span class="with">with</span>
      <span class="flavour f2">White Chocolate</span>
      <span class="flavour f3">&amp; Cashews</span>
      <span class="dotrule"></span>
    </div>
  </section>

  <section class="front mocha">
    <svg viewBox="0 0 380 260" width="380" height="260">
      <defs>
        <linearGradient id="bgMocha" x1="0" y1="0" x2="1" y2="1">
          <stop offset="0" stop-color="#e6dcc0"/><stop offset=".6" stop-color="#cdb88a"/><stop offset="1" stop-color="#9d7f4a"/>
        </linearGradient>
      </defs>
      <path d="M2 36 H70 Q120 2 190 2 Q260 2 310 36 H378 V248 H310 Q260 262 190 262 Q120 262 70 248 H2 Z" fill="url(#bgMocha)" stroke="#4a4644" stroke-width="3"/>
      <rect x="12" y="100" width="78" height="140" fill="#b58d5a" opacity=".45" role="img" aria-label="Illustration of wheat and oat ears"/>
      <rect x="292" y="100" width="78" height="140" fill="#a88656" opacity=".35" role="img" aria-label="Illustration of wheat and oat ears"/>
      <polygon points="95,82 285,82 285,238 190,222 95,238" fill="#3b3837" stroke="#fff" stroke-width="3"/>
    </svg>
    <div class="brand"><span class="name">Pem's</span><span class="sub">GRANOLA</span></div>
    <div class="copy">
      <span class="tagline">not only tasty, but good for you!</span>
      <span class="flavour f1">Mocha</span>
      <span class="flavour f2">Almond</span>
      <span class="dotrule"></span>
    </div>
  </section>

  <section class="back classic-bg">
    <div class="art" role="img" aria-label="Faint illustration of oat stalks" style="background:linear-gradient(180deg,rgba(210,190,150,0),rgba(210,190,150,.5))"></div>
    <div class="story">
      <span class="heading">Our Story</span>
      <div class="wheat" role="img" aria-label="Illustration of wheat ears"></div>
      <div class="mini-brand"><span class="name">Pem's</span><span class="sub">GRANOLA</span></div>
      <div class="web">www.website.com</div>
    </div>
    <div class="nutrition"><h2>Nutrition Facts</h2><span class="ingredients">INGREDIENTS:</span></div>
    <div class="upc">UPC Code</div>
  </section>

  <section class="back matcha-bg">
    <div class="art" role="img" aria-label="Faint illustration of oat stalks" style="background:linear-gradient(180deg,rgba(200,180,130,0),rgba(200,180,130,.45))"></div>
    <div class="story">
      <span class="heading">Our Story</span>
      <div class="wheat" role="img" aria-label="Illustration of wheat ears"></div>
      <div class="mini-brand"><span class="name">Pem's</span><span class="sub">GRANOLA</span></div>
      <div class="web">www.website.com</div>
    </div>
    <div class="nutrition"><h2>Nutrition Facts</h2><span class="ingredients">INGREDIENTS:</span></div>
    <div class="upc">UPC Code</div>
  </section>

  <section class="back mocha-bg">
    <div class="art" role="img" aria-label="Faint illustration of oat stalks" style="background:linear-gradient(180deg,rgba(150,120,70,0),rgba(150,120,70,.45))"></div>
    <div class="story">
      <span class="heading">Our Story</span>
      <div class="wheat" role="img" aria-label="Illustration of wheat ears"></div>
      <div class="mini-brand"><span class="name">Pem's</span><span class="sub">GRANOLA</span></div>
      <div class="web">www.website.com</div>
    </div>
    <div class="nutrition"><h2>Nutrition Facts</h2><span class="ingredients">INGREDIENTS:</span></div>
    <div class="upc">UPC Code</div>
  </section>

</main>
</body>
</html>
```